I am a Financial Adviser specialising in Aged Care Advice. We provide financial advice and assistance to families with loved ones entering an Aged Care facility.
We need a flyer detailing the Aged Care Packages that we offer. There will be 3 main packages & then other add ons. I need an area where the client can sign off on the package/s that they choose. I have attached a sample to demonstrate the required layout, and a copy of content. I would like the flyer to have an image as per the attached sample, and to be designed in soft pastels, blues, greens.

Financial

```html
<!DOCTYPE html>
<html lang="en">
<head>
<meta charset="utf-8">
<title>Extra Choice Options</title>
<link href="https://fonts.googleapis.com/css2?family=Luckiest+Guy&family=Ubuntu:wght@500&family=Nunito+Sans:wght@400;600&family=PT+Sans+Narrow:wght@400;700&display=swap" rel="stylesheet">
<style>
:root{
  --bg-top:#d4e4a4;
  --bg-bottom:#e6f08e;
  --gold:#dfb42a;
  --heading:#1f5e8a;
  --ink:#1e1e1e;
  --muted:#4c4c4c;
  --title:#3aaaea;
  --title-edge:#1b6fa8;
  --pink:#fde3ee;
  --white:#ffffff;
}
*{margin:0;padding:0;box-sizing:border-box}
html,body{width:881px;height:1200px;overflow:hidden}
body{background:linear-gradient(180deg,var(--bg-top) 0%,var(--bg-bottom) 100%);font-family:"Nunito Sans",Arial,sans-serif;color:var(--ink);position:relative}
.page-title{position:absolute;left:91px;top:18px;font-family:"Luckiest Guy",Impact,sans-serif;font-size:44px;letter-spacing:1px;color:var(--title);-webkit-text-stroke:1.5px var(--title-edge);text-shadow:2px 2px 0 var(--title-edge);font-weight:400}
.option{position:absolute;left:88px;width:758px;background:var(--white);border:3px solid var(--gold);padding:14px 20px 0 20px}
.option h2{font-family:"Ubuntu",Arial,sans-serif;font-weight:500;font-size:19.5px;color:var(--heading);margin-bottom:6px}
.option p{font-size:15.8px;line-height:21px}
.tickbox{position:absolute;left:37px;width:33px;height:33px;background:var(--white);border:3px solid var(--gold)}
.agreement{position:absolute;left:38px;top:830px;width:808px;height:218px;background:var(--pink);border:3px solid var(--gold);padding:9px 16px 0 16px;color:var(--muted);font-size:15.8px;line-height:26.4px}
.sig{position:absolute;text-align:center;font-size:13.5px;color:var(--ink)}
.sig .line{display:block;border-bottom:2px dotted #555;height:14px;margin-bottom:6px}
.fine{position:absolute;left:46px;top:1056px;width:800px;font-family:"PT Sans Narrow",Arial,sans-serif;font-size:14px;line-height:18px;color:var(--ink)}
.fine h3{font-size:17px;font-weight:700;margin-bottom:1px}
.fine p+p{margin-top:8px}
</style>
</head>
<body>
<h1 class="page-title">EXTRA CHOICE OPTIONS</h1>

<span class="tickbox" style="top:107px"></span>
<section class="option" style="top:74px;height:99px">
  <h2>CareLink/VSA Nominee $1,100</h2>
  <p>Communicate with CareLink/VSA on behalf of our client/s, and undertake all changes and updates to details, as directed by our client.</p>
</section>

<span class="tickbox" style="top:215px"></span>
<section class="option" style="top:182px;height:100px">
  <h2>Post Implementation Statement of Advice $1,650</h2>
  <p>Revise our original Advice Statement for any changes of circumstances including income &amp; asset variations, and provide further advice within the first 12 months of initial advice statement.</p>
</section>

<span class="tickbox" style="top:336px"></span>
<section class="option" style="top:291px;height:120px">
  <h2>Annual Review $990</h2>
  <p>A review of the recommendations made in our original advice document, &nbsp;taking into account any changes to client’s circumstances including checking current cash flow is sufficient to meet ongoing aged care costs.</p>
</section>

<span class="tickbox" style="top:451px"></span>
<section class="option" style="top:420px;height:98px">
  <h2>Post Entry Review $660</h2>
  <p>Review financial situation, check facility invoices are accurate, explain the Residential Aged Care Agreement and ensure all recommendations are implemented.</p>
</section>

<span class="tickbox" style="top:559px"></span>
<section class="option" style="top:527px;height:98px">
  <h2>Facility Liason $550</h2>
  <p>Negotiate with the Aged Care Facility regarding Accommodation payments, clarify &amp; explain Residential Care Agreement, and review facility invoices.</p>
</section>

<span class="tickbox" style="top:667px"></span>
<section class="option" style="top:634px;height:98px">
  <h2>Family Conferences $660</h2>
  <p>Facilitate &amp; co-ordinate family meetings to explain the Aged Care legislation and how it fits with the family circumstances.</p>
</section>

<span class="tickbox" style="top:763px"></span>
<section class="option" style="top:742px;height:78px">
  <h2>Estate Wrap $660</h2>
  <p>Assist beneficiaries with correct procedures and paperwork regarding the finalisation of the estate.</p>
</section>

<section class="agreement">
  <p>I/We have chosen the Service Package and Options as ticked above. &nbsp;I/We understand that by choosing the Essentials Package, that I/We are receiving factual information only, and not financial advice. I/We agree to pay the amount of ...................., within seven days of the date of the invoice received from Silverleaf Advice Co.</p>
  <div class="sig" style="left:18px;top:108px;width:183px"><span class="line"></span>Signature</div>
  <div class="sig" style="left:234px;top:108px;width:183px"><span class="line"></span>Signature</div>
  <div class="sig" style="left:451px;top:108px;width:183px"><span class="line"></span>Signature</div>
  <div class="sig" style="left:663px;top:108px;width:109px"><span class="line"></span>Date</div>
  <div class="sig" style="left:18px;top:170px;width:183px"><span class="line"></span>Adviser Signature</div>
  <div class="sig" style="left:234px;top:170px;width:109px"><span class="line"></span>Date</div>
</section>

<footer class="fine">
  <h3>Important Information</h3>
  <p>This document has been prepared by Silverleaf Advice Co Pty Ltd ABN 12 345 678 901, an Authorised Representative of Harbourline Licensee Limited ABN 98 765 432 109 AFSL 000000, a wholly owned, non-guaranteed subsidiary of the Southern Cross Mutual Bank ABN 11 222 333 444.</p>
  <p>Information in this document is based on current regulatory requirements and laws, as at 20 September, 2016 which may be subject to change. It contains general advice. It does not take in to account your individual objectives, financial situation or needs. You should consider talking to a financial adviser before making a financial decision.</p>
</footer>
</body>
</html>
```